Business Cards

Simple but professional looking business cards

Name: Rina Tolvardi
Title: Principle Lumen Platform Consultant
Email: r@kbrx.net.au
web : www.kbrx.net.au
Phone: +61.8.95203417
Mobile: +61.431862055
Updates

Hi All, Please include the office address Level 1, 200 Quarrington St, Kellerton, WA, 6191

Industry/Entity Type

Business

```html
<!DOCTYPE html>
<html lang="en">
<head>
<meta charset="utf-8">
<title>KBRX Business Cards</title>
<link href="https://fonts.googleapis.com/css2?family=Roboto:wght@400;500;700&display=swap" rel="stylesheet">
<style>
  :root {
    --page-bg: #e9e6e1;
    --card-white: #ffffff;
    --card-black: #0b0b0c;
    --brand-blue: #1f6fc4;
    --brand-green: #8cc63f;
    --text-blue: #2b63b0;
    --badge-red: #d9232e;
  }
  * { margin: 0; padding: 0; box-sizing: border-box; }
  html, body {
    width: 1200px; height: 858px; overflow: hidden;
    background: var(--page-bg);
    font-family: "Roboto", Arial, sans-serif;
  }
  .sheet {
    width: 1200px; height: 858px;
    display: flex; align-items: center; justify-content: center; gap: 40px;
  }
  .card {
    position: relative;
    width: 540px; height: 309px;
    border-radius: 4px;
    overflow: hidden;
    box-shadow: 0 6px 18px rgba(0,0,0,0.18);
  }
  .card-front { background: var(--card-white); }
  .card-back { background: var(--card-black); }

  .front-wave { position: absolute; inset: 0; }

  .brand-lockup {
    position: absolute;
    display: flex; align-items: center; gap: 10px;
  }
  .brand-dot { border-radius: 50%; background: var(--brand-blue); }
  .brand-name {
    font-weight: 400;
    color: var(--brand-blue);
    letter-spacing: 2px;
    line-height: 1;
  }
  .card-front .brand-lockup { top: 30px; left: 270px; }
  .card-front .brand-dot { width: 34px; height: 34px; }
  .card-front .brand-name { font-size: 54px; }

  .card-back .brand-lockup { top: 50%; left: 50%; transform: translate(-50%, -50%); }
  .card-back .brand-dot { width: 56px; height: 56px; }
  .card-back .brand-name { font-size: 92px; }

  .office-address {
    position: absolute; top: 102px; right: 52px;
    text-align: right; color: var(--text-blue);
    font-size: 13px; line-height: 17px;
  }
  .contact-list {
    position: absolute; top: 146px; right: 26px;
    list-style: none; color: var(--text-blue);
    font-size: 12.5px; line-height: 17px;
  }
  .contact-list li {
    display: flex; justify-content: flex-end; align-items: center; gap: 10px;
  }
  .contact-icon { width: 12px; height: 12px; flex: none; }

  .partner-badge {
    position: absolute; top: 226px; left: 372px;
    width: 74px; height: 22px;
    background: var(--badge-red);
  }

  .holder {
    position: absolute; left: 30px; bottom: 22px;
    color: var(--card-white);
  }
  .holder-name { font-size: 20px; font-weight: 500; line-height: 24px; }
  .holder-title { font-size: 12.5px; line-height: 15px; }
</style>
</head>
<body>
<main class="sheet">
  <section class="card card-front">
    <svg class="front-wave" width="540" height="309" viewBox="0 0 540 309">
      <defs>
        <linearGradient id="waveBlue" x1="0" y1="0" x2="1" y2="0.4">
          <stop offset="0" stop-color="#1a62b8"/>
          <stop offset="0.5" stop-color="#3a8fd6"/>
          <stop offset="1" stop-color="#1c5fae"/>
        </linearGradient>
      </defs>
      <path d="M0 176 C 90 236, 260 268, 430 270 L 540 268 L 540 309 L 0 309 Z" fill="url(#waveBlue)"/>
      <path d="M0 164 C 90 224, 260 258, 430 262 L 540 262" fill="none" stroke="#8cc63f" stroke-width="4"/>
    </svg>

    <div class="brand-lockup">
      <span class="brand-dot"></span>
      <span class="brand-name">KBRX</span>
    </div>

    <p class="office-address">Level 1, 200 Quarrington St,<br>Kellerton, WA, 6191</p>

    <ul class="contact-list">
      <li>r@kbrx.net.au
        <svg class="contact-icon" viewBox="0 0 12 12"><rect x="0.5" y="2" width="11" height="8" rx="1" fill="#8cc63f"/><path d="M1 2.5 L6 7 L11 2.5" fill="none" stroke="#fff" stroke-width="1"/></svg>
      </li>
      <li>www.kbrx.net.au
        <svg class="contact-icon" viewBox="0 0 12 12"><circle cx="6" cy="6" r="5.5" fill="#8cc63f"/><path d="M0.5 6 H11.5 M6 0.5 C3 3.5,3 8.5,6 11.5 M6 0.5 C9 3.5,9 8.5,6 11.5" fill="none" stroke="#fff" stroke-width="0.8"/></svg>
      </li>
      <li>+61.8.95203417
        <svg class="contact-icon" viewBox="0 0 12 12"><path d="M2.5 1 L4.5 1 L5.5 4 L4 5 C4.8 6.8 5.2 7.2 7 8 L8 6.5 L11 7.5 L11 9.5 C11 10.5 10 11 9 11 C4.5 10.5 1.5 7.5 1 3 C1 2 1.5 1 2.5 1 Z" fill="#8cc63f"/></svg>
      </li>
      <li>+61.431862055
        <svg class="contact-icon" viewBox="0 0 12 12"><rect x="3" y="0.5" width="6" height="11" rx="1" fill="#8cc63f"/><rect x="4" y="2" width="4" height="7" fill="#fff"/></svg>
      </li>
    </ul>

    <div class="partner-badge" role="img" aria-label="Partner badge"></div>

    <div class="holder">
      <p class="holder-name">Rina Tolvardi</p>
      <p class="holder-title">Principle Lumen Platform<br>Consultant</p>
    </div>
  </section>

  <section class="card card-back">
    <div class="brand-lockup">
      <span class="brand-dot"></span>
      <span class="brand-name">KBRX</span>
    </div>
  </section>
</main>
</body>
</html>
```